Online Nutrition Consulting Website/healthy lifestyle

This is a website for online nutrition consulting. (For example, weight loss.) The company is called Mirela's. I included the logo so you have a feel for the colors and the message of the company. I would like to have one main neutral color in there. (I am leaning toward grey, but I am open to ideas) I would like the design to be simple and to the point.

My ultimate goal is for my website to stand out from other nutrition websites by projecting my slogan (It's not a diet. It's a lifestyle.)

Target Market(s)

Health-conscious people.

Industry/Entity Type

Nutrition

Coding

Coded - Design and coding required

Number of Pages Required

4 page

Font styles to use
Script

Requirements
Must have
• Home page, Services page , About page, and a Blog page. (Once I see the layout, I will give you more detail so it isn't confusing. For example: payment of services and the "About me")
• Logo must be included.
• Easy navigation. Not too much scrolling.

```html
<!DOCTYPE html>
<html lang="en">
<head>
<meta charset="utf-8">
<title>Mirela's — Nutrition Consulting</title>
<link href="https://fonts.googleapis.com/css2?family=Open+Sans:wght@400;600;700;800&display=swap" rel="stylesheet">
<style>
:root{
  --green:#3aaa35;
  --green-dark:#2a8a27;
  --green-light:#8cd14a;
  --grey-text:#6d6d6d;
  --grey-dark:#333;
  --grey-line:#e2e2e2;
  --footer-bg:#f1f1f1;
  --white:#fff;
}
*{box-sizing:border-box;margin:0;padding:0}
html,body{width:1200px;height:2236px;overflow:hidden}
body{font-family:'Open Sans',Arial,sans-serif;color:var(--grey-text);background:var(--white);position:relative}
.wrap{width:1040px;margin:0 auto;position:relative}
a{color:inherit;text-decoration:none}

/* header */
.site-header{height:185px}
.brand{position:absolute;left:20px;top:40px;display:flex;align-items:center;gap:14px}
.brand-dot{width:44px;height:44px;border-radius:50%;background:var(--green)}
.brand-name{font-size:44px;font-weight:700;color:var(--green);line-height:1}
.brand-tag{position:absolute;left:78px;top:98px;font-size:11px;letter-spacing:2px;color:var(--grey-text);font-weight:600}
.util-links{position:absolute;right:0;top:12px;display:flex;gap:34px;font-size:12px}
.search{position:absolute;right:0;top:108px;width:200px;height:28px;border:1px solid var(--grey-line);font-size:11px;padding:6px 10px;color:#aaa;display:flex;justify-content:space-between;align-items:center}
.search svg{width:12px;height:12px}

/* nav */
.main-nav{background:var(--green);height:32px}
.main-nav ul{list-style:none;display:flex;height:32px;width:1040px;margin:0 auto}
.main-nav li{flex:1;text-align:center;color:var(--white);font-size:12px;font-weight:600;line-height:32px}
.main-nav li.active{background:var(--green-dark)}

/* hero */
.hero{height:548px;position:relative;background:linear-gradient(90deg,#c9b7a6 0%,#d8c4b0 35%,#b98f74 60%,#e6dcd2 100%);overflow:hidden}
.hero-text{position:absolute;left:80px;top:186px}
.hero-title{font-size:54px;font-weight:800;color:var(--white);letter-spacing:1px}
.hero-sub{font-size:28px;font-weight:800;color:var(--green-light);margin-top:6px;padding-left:40px}
.hero-arrow{position:absolute;top:250px;width:36px;height:36px;border-radius:50%;background:rgba(255,255,255,.55)}
.hero-arrow.left{left:24px}.hero-arrow.right{right:24px}
.hero-arrow svg{width:36px;height:36px}

/* intro */
.intro{height:316px;padding-top:58px}
.intro-copy{width:740px}
h2.section-title{font-size:21px;font-weight:800;color:var(--grey-dark)}
.intro-lead{font-size:20px;font-weight:600;color:var(--green);margin:6px 0 12px}
p.body{font-size:12.5px;line-height:1.6}
.btn{display:inline-flex;align-items:center;gap:6px;background:var(--green);color:var(--white);font-size:12px;font-weight:600;padding:7px 16px}
.intro .btn{margin-top:18px}
.intro-photo{position:absolute;right:20px;top:10px;width:210px;height:200px;border:6px solid var(--white);box-shadow:0 0 0 1px var(--grey-line);background:linear-gradient(135deg,#e7c8b8,#c9868f 60%,#f2e6e2)}

/* services */
.services{height:370px;padding-top:20px}
.service-grid{display:flex;gap:20px;margin-top:30px}
.service{width:245px}
.service-photo{height:168px;border:5px solid var(--white);box-shadow:0 0 0 1px var(--grey-line)}
.service-title{font-size:13.5px;font-weight:800;color:var(--green);margin:18px 0 6px;text-align:center}
.service p.body{font-size:11.5px;text-align:center}
.service .btn{margin:14px auto 0;display:flex;width:110px;justify-content:center}

.divider{border-top:1px solid var(--grey-line);width:1040px;margin:0 auto}

/* about + news */
.about-news{height:320px;padding-top:46px;display:flex;gap:40px}
.about{width:780px}
.about-row{display:flex;gap:30px;margin-top:20px}
.about-photo{width:260px;height:160px;border:5px solid var(--white);box-shadow:0 0 0 1px var(--grey-line);background:linear-gradient(135deg,#e6eef3,#9fb7c9 55%,#f4f4f4)}
.about-copy{flex:1}
.about-lead{font-size:15px;font-weight:600;color:var(--grey-dark);margin-bottom:8px}
.more{display:block;margin-top:14px;font-size:12px;color:var(--green)}
.news{flex:1}
.news-date{margin-top:20px;font-size:12px;color:var(--grey-dark)}
.news-title{font-size:14px;font-weight:700;color:var(--grey-dark);margin:4px 0 6px}

/* footer */
.site-footer{background:var(--footer-bg);height:340px;padding-top:36px}
.footer-cols{display:flex;gap:40px}
.footer-col{width:230px}
.footer-col h4{font-size:12px;font-weight:800;color:var(--grey-dark);margin-bottom:14px}
.footer-col ul{list-style:none;font-size:11px;line-height:2}
.newsletter-input{height:28px;border:1px solid var(--grey-line);background:var(--white);font-size:11px;padding:6px 10px;color:#aaa;display:flex;justify-content:space-between}
.social{display:flex;gap:12px;margin-top:6px}
.social span{width:32px;height:32px;border-radius:50%;background:var(--green)}
.bottom-bar{position:absolute;left:0;right:0;bottom:0;height:64px;background:var(--green);color:var(--white);font-size:11px}
.bottom-bar .wrap{display:flex;justify-content:center;align-items:center;height:64px}
.to-top{position:absolute;right:0}
</style>
</head>
<body>

<header class="site-header wrap">
  <div class="brand"><span class="brand-dot"></span><span class="brand-name">Mirela's</span></div>
  <div class="brand-tag">IT'S NOT A DIET · IT'S A LIFESTYLE</div>
  <nav class="util-links"><a>My Account</a><a>My Wishlist</a><a>Checkout</a><a>Log in</a></nav>
  <div class="search">Search entire store here...
    <svg viewBox="0 0 12 12"><circle cx="5" cy="5" r="3.5" fill="none" stroke="#999" stroke-width="1.5"/><line x1="7.5" y1="7.5" x2="11" y2="11" stroke="#999" stroke-width="1.5"/></svg>
  </div>
</header>

<nav class="main-nav">
  <ul>
    <li class="active">HOME</li><li>ABOUT US</li><li>SERVICES</li><li>TRAINER</li><li>BLOG</li><li>CONTACT US</li>
  </ul>
</nav>

<section class="hero" role="img" aria-label="Photo of a smiling woman eating a fresh salad">
  <div class="hero-text">
    <div class="hero-title">IT'S NOT A DIET</div>
    <div class="hero-sub">IT'S A LIFESTYLE</div>
  </div>
  <span class="hero-arrow left"><svg viewBox="0 0 36 36"><path d="M21 11l-7 7 7 7" fill="none" stroke="#fff" stroke-width="3"/></svg></span>
  <span class="hero-arrow right"><svg viewBox="0 0 36 36"><path d="M15 11l7 7-7 7" fill="none" stroke="#fff" stroke-width="3"/></svg></span>
</section>

<section class="intro wrap">
  <div class="intro-copy">
    <h2 class="section-title">NUTRITION CONSULTING COMPANY MIRELA'S</h2>
    <div class="intro-lead">Temporibus autem quibusdam et aut officiis</div>
    <p class="body">Nam libero tempore, cum soluta nobis est eligendi optio cumque nihil impedit quo minus id quod maxime placeat facere possimus, omnis voluptas assumenda est, omnis dolor repellendus. Temporibus autem quibusdam et aut officiis debitis aut rerum necessitatibus saepe eveniet ut et voluptates repudiandae sint et molestiae non recusandae.</p>
    <a class="btn">Read More ›</a>
  </div>
  <div class="intro-photo" role="img" aria-label="Photo of a woman relaxing on a sofa"></div>
</section>

<section class="services wrap">
  <h2 class="section-title">OUR SERVICES</h2>
  <div class="service-grid">
    <div class="service">
      <div class="service-photo" role="img" aria-label="Photo of a woman exercising outdoors" style="background:linear-gradient(135deg,#9ccbe8,#d9b79c 70%,#8fae6a)"></div>
      <div class="service-title">ET HARUM QUIDEM</div>
      <p class="body">Nam libero tempore, cum soluta nobis est eligendi optio cumque nihil impedit quo minus.</p>
      <a class="btn">Show More ›</a>
    </div>
    <div class="service">
      <div class="service-photo" role="img" aria-label="Photo of women stretching together" style="background:linear-gradient(135deg,#e9e4dc,#d8b49a 55%,#b9a48e)"></div>
      <div class="service-title">VOLUPTATES REPUDIANDAE</div>
      <p class="body">Nam libero tempore, cum soluta nobis est eligendi optio cumque nihil impedit quo minus.</p>
      <a class="btn">Show More ›</a>
    </div>
    <div class="service">
      <div class="service-photo" role="img" aria-label="Photo of a runner at sunset" style="background:linear-gradient(135deg,#f3b45d,#c86f3a 55%,#6f4b34)"></div>
      <div class="service-title">TEMPORIBUS AUTEM</div>
      <p class="body">Nam libero tempore, cum soluta nobis est eligendi optio cumque nihil impedit quo minus.</p>
      <a class="btn">Show More ›</a>
    </div>
    <div class="service">
      <div class="service-photo" role="img" aria-label="Photo of a woman resting on a beach" style="background:linear-gradient(135deg,#cfe6ef,#e9d7c0 60%,#c4a888)"></div>
      <div class="service-title">EXEGUQE SUNT</div>
      <p class="body">Nam libero tempore, cum soluta nobis est eligendi optio cumque nihil impedit quo minus.</p>
      <a class="btn">Show More ›</a>
    </div>
  </div>
</section>

<div class="divider"></div>

<section class="about-news wrap">
  <div class="about">
    <h2 class="section-title">ABOUT US</h2>
    <div class="about-row">
      <div class="about-photo" role="img" aria-label="Photo of a smiling consultant at a desk"></div>
      <div class="about-copy">
        <div class="about-lead">Neque porro quisquam est, qui dolorem ipsum</div>
        <p class="body">Nam libero tempore, cum soluta nobis est eligendi optio cumque nihil impedit quo minus id quod maxime placeat facere possimus. Nam libero tempore, cum soluta nobis est eligendi optio cumque nihil impedit quo minus id quod maxime placeat facere possimus, omnis dolor repellendus.</p>
        <a class="more">Read more</a>
      </div>
    </div>
  </div>
  <div class="news">
    <h2 class="section-title">LATEST NEWS</h2>
    <div class="news-date">01.06.2015</div>
    <div class="news-title">Temporibus autem quibusdam et</div>
    <p class="body">Omnis voluptas assumenda est, omnis dolor repellendus temporibus autem quibusdam.</p>
    <a class="more">Read more</a>
  </div>
</section>

<footer class="site-footer">
  <div class="wrap footer-cols">
    <div class="footer-col">
      <h4>INFORMATION</h4>
      <ul><li>About Us</li><li>Customer Service</li><li>Template Settings</li><li>Privacy Policy</li><li>Site Map</li><li>Search Terms</li><li>Advanced Search</li><li>Orders and Returns</li><li>Contact Us</li></ul>
    </div>
    <div class="footer-col">
      <h4>WHY BUY FROM US</h4>
      <ul><li>Shipping &amp; Returns</li><li>Secure Shopping</li><li>International Shipping</li><li>Affiliates</li><li>Group Sales</li></ul>
    </div>
    <div class="footer-col">
      <h4>MY ACCOUNT</h4>
      <ul><li>Shipping &amp; Returns</li><li>Secure Shopping</li><li>International Shipping</li><li>Affiliates</li><li>Group Sales</li></ul>
    </div>
    <div class="footer-col">
      <h4>NEWSLETTER SIGN UP</h4>
      <div class="newsletter-input">Enter your Email <span>›</span></div>
      <h4 style="margin-top:26px">FOLLOW US</h4>
      <div class="social"><span></span><span></span><span></span><span></span></div>
    </div>
  </div>
  <div class="bottom-bar">
    <div class="wrap">© 2015 Mirela's. All Rights Reserved.<span class="to-top">Top ˄</span></div>
  </div>
</footer>

</body>
</html>
```